Product Label & Logo for New Supplement

Your design will automatically be eliminated if you do NOT read this brief, because the description tells you about the brand you will be creating an identity for.Attached is the current label for the product. It is boring and doesn’t tell a story.We need you to unleash creative work to help patients with chronic pain diseases - like Multiple Sclerosis, Chronic Fatigue Syndrome, Lupus, and Fibromyalgia - no longer be defined by their disease. Qorvi Blend is a new supplement developed by a neurologist to help patients with chronic pain feel better and have better days. It increases energy and stamina, saving the patient from having to take upwards of 40 different supplements.The label and logo need to convey that this supplement will give hurting patients new life.
Updates
Went on vacation/holiday
Target Market(s)
People with fatigue, pain and inflammation
Industry/Entity Type
Supplement
Requirements
Must have
- Gender neutral, eye catching, all the ingredients listed in addition to logo design
Nice to have
- Custom logo, no generic fonts for name brand

```html
<!DOCTYPE html>
<html lang="en">
<head>
<meta charset="utf-8">
<title>Qorvi Blend – Supplement Label</title>
<link href="https://fonts.googleapis.com/css2?family=Montserrat:wght@600;700&family=Roboto+Condensed:wght@400;700&display=swap" rel="stylesheet">
<style>
  :root {
    --navy: #1f2d5c;
    --navy-deep: #172349;
    --teal: #2aaeb3;
    --ink: #2b2b2b;
    --rule: #3a3a3a;
    --soft: #e9ebef;
    --page: #ffffff;
    --photo-a: #6b3f63;
    --photo-b: #3a4a86;
  }
  * { margin: 0; padding: 0; box-sizing: border-box; }
  html, body { width: 1032px; height: 1200px; overflow: hidden; background: var(--page); }
  body { font-family: "Roboto Condensed", "Arial Narrow", sans-serif; color: var(--ink); position: relative; }

  .label { position: absolute; left: 0; top: 380px; width: 1032px; height: 440px; background: var(--page); }
  .label-shapes { position: absolute; inset: 0; }
  .abs { position: absolute; }

  /* left panel */
  .directions, .caution { left: 25px; width: 292px; font-size: 12.5px; line-height: 1.35; text-align: justify; }
  .directions { top: 16px; }
  .caution { top: 64px; }
  .lead { color: var(--teal); }
  .warning { left: 25px; top: 206px; width: 300px; font-size: 11px; font-weight: 700; line-height: 1.35; }
  .disclaimer { left: 28px; top: 254px; width: 292px; padding: 5px 8px; background: var(--soft); border-radius: 4px; font-size: 9.5px; line-height: 1.3; }
  .distributor { left: 25px; top: 330px; color: #fff; font-size: 12px; line-height: 1.3; }
  .distributor strong { font-weight: 700; }
  .website { left: 90px; top: 400px; color: #fff; font-size: 14px; }

  /* centre panel */
  .brand-small { left: 355px; top: 20px; display: flex; align-items: center; gap: 7px; font-family: "Montserrat", sans-serif; font-weight: 700; font-size: 21px; color: var(--navy); letter-spacing: 0.5px; }
  .brand-mark { width: 14px; height: 14px; background: var(--teal); }
  .brand-title { left: 330px; top: 122px; width: 370px; text-align: center; font-family: "Montserrat", sans-serif; font-weight: 700; font-size: 37px; color: var(--navy); letter-spacing: 0.5px; }
  .tagline { left: 330px; top: 168px; width: 370px; text-align: center; font-family: "Montserrat", sans-serif; font-weight: 600; font-size: 11.5px; letter-spacing: 1.2px; color: var(--navy); }
  .benefits { left: 484px; top: 276px; list-style: none; color: #fff; font-size: 16.5px; line-height: 26.5px; letter-spacing: 0.3px; }
  .benefits li::before { content: "• "; }
  .product-type { left: 482px; top: 376px; font-size: 14.5px; line-height: 19px; color: var(--ink); }
  .product-type b { font-weight: 700; }

  /* supplement facts */
  .facts { left: 725px; top: 34px; width: 293px; font-size: 10.5px; line-height: 1.28; }
  .facts h2 { font-family: "Roboto Condensed", sans-serif; font-weight: 400; font-size: 25px; line-height: 1; color: var(--ink); margin-bottom: 6px; }
  .facts .rule { border-top: 1px solid var(--rule); margin: 4px 0; }
  .facts .rule.thick { border-top-width: 2px; }
  .facts table { width: 100%; border-collapse: collapse; }
  .facts td { padding: 0; vertical-align: top; }
  .facts .amt { text-align: right; padding-right: 14px; white-space: nowrap; }
  .facts .dv { text-align: right; width: 46px; }
  .facts .head td { padding: 2px 0; }
  .other { left: 725px; top: 302px; width: 293px; font-size: 10.5px; line-height: 1.25; }
  .recycle { left: 740px; top: 386px; display: flex; gap: 12px; }
  .recycle span { width: 24px; height: 24px; border: 3px solid var(--ink); border-radius: 50%; display: block; }
</style>
</head>
<body>
<main class="label">
  <svg class="label-shapes" width="1032" height="440" viewBox="0 0 1032 440">
    <defs>
      <linearGradient id="nerve-tones" x1="0" y1="0" x2="1" y2="1">
        <stop offset="0" stop-color="#3a4a86"/>
        <stop offset="0.5" stop-color="#6b3f63"/>
        <stop offset="1" stop-color="#172349"/>
      </linearGradient>
    </defs>
    <path d="M560 0 C610 0 630 22 700 22 H1032 V0 Z" fill="#1f2d5c"/>
    <path d="M0 312 H300 C360 312 390 264 450 264 H708 V372 H475 V440 H0 Z" fill="#1f2d5c"/>
    <path role="img" aria-label="Close-up photo of a glowing nerve cell in pink and blue tones"
          d="M330 290 C380 270 400 264 450 264 H520 C505 300 490 340 475 372 V440 H330 Z"
          fill="url(#nerve-tones)" opacity="0.9"/>
  </svg>

  <p class="abs directions"><span class="lead">DIRECTIONS :</span> Take two (2) tablets in the morning or take the first tablet at breakfast and the second at lunch.</p>
  <p class="abs caution"><span class="lead">CAUTION :</span> Do not exceed recommended dose. Pregnant or nursing mother, children under the age of 18, and individuals with a known medical condition should consult a physician before using this or any dietary supplement.</p>
  <p class="abs warning">KEEP OUT OF REACH OF CHILDREN. DO NOT USE IF SAFETY SEAL IS DAMAGED OR MISSING. STORE IN A COOL, DRY PLACE.</p>
  <p class="abs disclaimer">*These statements have not been evaluated by the food and drug administration. This product is not intended to diagnose, treat, cure or prevent any disease.</p>
  <p class="abs distributor">DISTRIBUTED BY :<br><strong>Qorvi Blend</strong><br>info@qorvi-labs.com</p>
  <p class="abs website">www.qorvi-labs.com</p>

  <div class="abs brand-small"><span class="brand-mark"></span>QORVI BLEND</div>
  <h1 class="abs brand-title">QORVI BLEND</h1>
  <p class="abs tagline">DON'T BE DEFINED BY YOUR ILLNESS</p>
  <ul class="abs benefits">
    <li>INCREASES ENERGY</li>
    <li>DECREASES INFLAMMATION</li>
    <li>IMPROVES PERFORMANCE</li>
  </ul>
  <p class="abs product-type">DIETARY SUPPLEMENT<br><b>60 TABLETS</b></p>

  <section class="abs facts">
    <h2>SUPPLEMENT FACTS</h2>
    <p>Serving Size : 2 Tablets<br>Serving per Container : 30</p>
    <div class="rule thick"></div>
    <table>
      <tr class="head"><td>Amount per Serving</td><td class="amt">%Daily</td><td class="dv">Value</td></tr>
    </table>
    <div class="rule"></div>
    <table>
      <tr><td>Vitamin C (Ascorbic Acid)</td><td class="amt">500 mg</td><td class="dv">556%</td></tr>
      <tr><td>Vitamin D3 (as Cholecalciferol)</td><td class="amt">5000 IU</td><td class="dv">625%</td></tr>
      <tr><td>Folate</td><td class="amt">1,666.67 mcg DFE</td><td class="dv">417%</td></tr>
      <tr><td></td><td class="amt">(1000 mcg Folic Acid)</td><td class="dv">151%</td></tr>
      <tr><td>Vitamin B12 (as Cyanocobalamin)</td><td class="amt">2000 mcg</td><td class="dv">83,333%</td></tr>
      <tr><td>Biotin</td><td class="amt">300 mcg</td><td class="dv">1000%</td></tr>
    </table>
    <div class="rule"></div>
    <table>
      <tr><td>Proprietary Blend</td><td class="amt">1130 mg</td><td class="dv">*</td></tr>
    </table>
    <p>N-Acetyl-L-Cysteine, Turmeric Root Extract, Green Coffee Bean Extract<br>Folic acid</p>
    <div class="rule thick"></div>
    <p>*Daily Value not established.</p>
  </section>
  <p class="abs other">Other Ingredients : Microcrystalline Cellulose, Stearic Acid, Dicalcium Phosphate, Croscarmellose Sodium, Magnesium Stearate, Silicon Dioxide, Pharmaceutical Glaze (Shellac, Povidone).</p>
  <div class="abs recycle" aria-hidden="true"><span></span><span></span></div>
</main>
</body>
</html>
```